New Business Cards for MB&LR

We need updated business cards for a staff of 15 engineers, estimators, project managers, and sales people. We have recently begun changes to our website and marketing material to improve our look and branding. We are an established fabricator specializing in pressure vessels, tanks, and structural steel. The owners require us to use the existing logo and old english text design. Also, we prefer dark grey or mostly black cards.
Target Market(s)
Engineers, purchasing agents, estimators, and project managers of; mining companies, refineries, industrial construction professionals
Industry/Entity Type
Business
Contact Information for Business Card
Logo, phone, website, email, etc.
Look and feel

```html
<!DOCTYPE html>
<html lang="en">
<head>
<meta charset="utf-8">
<title>MB&amp;LR Business Cards</title>
<link href="https://fonts.googleapis.com/css2?family=UnifrakturMaguntia&family=Libre+Baskerville&display=swap" rel="stylesheet">
<style>
  :root {
    --backdrop: #1c1b1c;
    --card-dark: #2e2b2c;
    --card-dark-edge: #1f1d1e;
    --card-light: #f1f0ee;
    --ink-dark: #2a2a2a;
    --ink-light: #e6e6e6;
    --watermark: #e0dfdc;
  }
  html, body {
    margin: 0;
    width: 1200px;
    height: 900px;
    overflow: hidden;
    background: var(--backdrop);
  }
  .canvas {
    position: relative;
    width: 1200px;
    height: 900px;
  }
  .card {
    position: absolute;
    left: 250px;
    width: 700px;
    height: 400px;
    border-radius: 26px;
    overflow: hidden;
    box-shadow: 0 14px 40px rgba(0,0,0,0.55);
  }
  .card--front {
    top: 40px;
    background: linear-gradient(160deg, var(--card-dark) 0%, var(--card-dark-edge) 100%);
  }
  .card--back {
    top: 460px;
    background: var(--card-light);
  }
  .brand-mark {
    display: flex;
    align-items: center;
    gap: 10px;
    font-family: "Libre Baskerville", serif;
    font-size: 18px;
    letter-spacing: 1px;
  }
  .brand-mark__square {
    width: 22px;
    height: 22px;
    border: 2px solid currentColor;
  }
  .company-name {
    font-family: "UnifrakturMaguntia", serif;
    line-height: 1.05;
  }
  /* front */
  .card--front .lockup {
    position: absolute;
    left: 170px;
    top: 120px;
    color: var(--ink-light);
  }
  .card--front .company-name {
    font-size: 46px;
    margin-top: 18px;
  }
  .card--front .watermark {
    position: absolute;
    right: -20px;
    bottom: -30px;
    font-family: "Libre Baskerville", serif;
    font-size: 150px;
    color: rgba(255,255,255,0.04);
  }
  /* back */
  .card--back .lockup {
    position: absolute;
    left: 50px;
    top: 44px;
    color: var(--ink-dark);
  }
  .card--back .company-name {
    font-size: 34px;
    margin-top: 14px;
  }
  .card--back .watermark {
    position: absolute;
    right: -30px;
    bottom: -40px;
    font-family: "Libre Baskerville", serif;
    font-size: 150px;
    color: var(--watermark);
  }
  .contact {
    position: absolute;
    left: 380px;
    top: 210px;
    font-family: "Libre Baskerville", serif;
    color: var(--ink-dark);
    font-size: 16px;
    line-height: 1.55;
  }
  .contact__name {
    font-family: "UnifrakturMaguntia", serif;
    font-size: 30px;
    line-height: 1.1;
    margin-bottom: 4px;
  }
</style>
</head>
<body>
<div class="canvas">
  <section class="card card--front">
    <div class="watermark" aria-hidden="true">MB&amp;LR</div>
    <div class="lockup">
      <div class="brand-mark"><span class="brand-mark__square"></span>MB&amp;LR</div>
      <div class="company-name">Midvale Beam &amp;<br>Ledge Rolling</div>
    </div>
  </section>

  <section class="card card--back">
    <div class="watermark" aria-hidden="true">MB&amp;LR</div>
    <div class="lockup">
      <div class="brand-mark"><span class="brand-mark__square"></span>MB&amp;LR</div>
      <div class="company-name">Midvale Beam &amp;<br>Ledge Rolling</div>
    </div>
    <div class="contact">
      <div class="contact__name">Daniel Whitcombe</div>
      <div>Project Manager</div>
      <div>555.014.2271</div>
      <div>info@mbandlr.com</div>
      <div>www.mbandlr.com</div>
    </div>
  </section>
</div>
</body>
</html>
```